依頼詳細
色々なホームページを参考に骨組みを作ってみました。
PDFファイルで添付しています。
2列から3列に変わると面白いのかなと思い、作りました。
もっと良い見せ方などがあれば自由に変更して頂いて構いません。

医院情報(院名・住所・診療時間)も添付資料をご覧ください。

ホームページには…
①まずは新患様に来ていただく(集客)
②医院の知名度の向上
このような効果を期待しています。

希望カラー…
建物の外装はこげ茶・白というモダンな作りです。
看板はオレンジ色です。
まだ医院が工事中で完成しておりませんが、
・完成イメージ
・現在出来上がっている院内
の写真を添付しておりますので、お色味の参考にして頂きたいです。

素材サイト:ピクセリオ「https://jp.pixelrio-stock.com/
このサイトの定期契約を当院で行いましたので
定期契約内で利用できる写真をデザイン内で使用してください。

他に必要なお写真がある場合には、無料で商用利用が出来るものを
ご利用頂ければと思います。

その他必要な情報などございましたらご質問ください。
楽しみにお待ちしております。宜しくお願い致します。
希望イメージ
シンプル 複雑
単色 カラフル
暗い 明るい
日常 高級
遊び心 厳粛
未来的 伝統的
女性的 男性的
希望する色
茶系、黄・オレンジ系、ベースカラーはクリーム色ぐらいのホワイトが希望です。
納品ファイル
• 高解像度JPG (.jpg)
• イラストレーター形式 (.ai)
• フォトショップ形式 (.psd)
• PNG形式 (.png)
ランサーの皆さま

お世話になっております。
素敵なデザインをご提案頂き誠にありがとうございます。
とても嬉しいです!

期間が短く、申し訳ございません。
募集期間が延長出来るという事で、今日から1週間ほど期間を延長致します。

こちらの提出した骨組みから全く違う構成でももちろん構いませんので、
色んなパターンのデザインが見てみたいと思っています。
引き続きよろしくお願い致します。
■ 選んだ理由

一番当院のイメージに近く、一番要望に沿っているデザインだと感じたため。

■ 提案者全員のお礼・コメント

たくさんのデザインをご提案頂き、非常にうれしく思っております。
OPENに向けまずはトップデザインが決まり、わくわくしております。

この度は誠にありがとうございました。
これからも皆様のご活躍を、陰ながらではございますが、応援致しております。

```html
<!DOCTYPE html>
<html lang="ja">
<head>
<meta charset="utf-8">
<title>ひなた歯科クリニック</title>
<link href="https://fonts.googleapis.com/css2?family=M+PLUS+Rounded+1c:wght@400;500;700;800&family=Noto+Sans+JP:wght@400;500;700&display=swap" rel="stylesheet">
<style>
:root{
  --orange:#ec7a2c;
  --orange-soft:#f6a25a;
  --orange-pale:#fde6cf;
  --brown:#5b3a23;
  --brown-soft:#8a6a52;
  --cream:#fbf5e9;
  --line:#e8dccb;
  --text:#4a3a2e;
  --white:#ffffff;
}
*{box-sizing:border-box;margin:0;padding:0}
html,body{width:1200px;height:2280px;overflow:hidden}
body{background:var(--white);font-family:"Noto Sans JP",sans-serif;color:var(--text);font-size:14px;position:relative}
.round{font-family:"M PLUS Rounded 1c",sans-serif}

.site-header{position:absolute;top:0;left:0;width:1200px;height:98px}
.brand{position:absolute;left:120px;top:18px}
.brand-tag{font-size:12px;color:var(--brown-soft)}
.brand-name{display:flex;align-items:center;gap:10px;margin-top:4px;font-family:"M PLUS Rounded 1c",sans-serif;font-weight:800;font-size:30px;color:var(--orange)}
.brand-mark{width:22px;height:22px;border-radius:50%;background:var(--orange)}
.hours{position:absolute;left:540px;top:26px;font-size:13px;line-height:1.6;color:var(--text)}
.contact{position:absolute;right:100px;top:18px;text-align:right}
.contact small{display:block;font-size:12px;color:var(--brown-soft)}
.tel{display:flex;align-items:center;gap:6px;justify-content:flex-end;font-family:"M PLUS Rounded 1c",sans-serif;font-weight:800;font-size:30px;color:var(--orange)}
.contact .addr{font-size:11px;color:var(--brown-soft);margin-top:2px}

.global-nav{position:absolute;top:98px;left:120px;width:960px;height:44px;display:flex;border-top:1px solid var(--line);border-bottom:1px solid var(--line)}
.global-nav a{flex:1;display:flex;align-items:center;justify-content:center;font-size:14px;color:var(--brown);text-decoration:none;border-left:1px solid var(--line)}
.global-nav a:first-child{flex:0 0 70px;border-left:none}

.hero{position:absolute;top:150px;left:0;width:1200px;height:560px;overflow:hidden}
.hero-side{position:absolute;top:0;height:560px;width:120px;background:linear-gradient(135deg,#d9e9f0,#f4ede2);opacity:.55}
.hero-main{position:absolute;left:120px;top:0;width:960px;height:560px;background:linear-gradient(120deg,#e6f1f5 0%,#f7f3ec 45%,#f2e2cf 100%)}
.hero-copy{position:absolute;left:200px;top:430px;font-family:"M PLUS Rounded 1c",sans-serif;font-weight:800;font-size:30px;line-height:1.5;color:var(--orange)}
.hero-copy span{display:inline-block;background:rgba(255,255,255,.82);padding:2px 14px;margin-bottom:6px}
.dots{position:absolute;top:726px;left:0;width:1200px;display:flex;justify-content:center;gap:14px}
.dots i{width:12px;height:12px;border-radius:50%;background:#d9d2c8}
.dots i:first-child{background:var(--brown-soft)}

.services{position:absolute;top:770px;left:120px;width:960px;display:flex;gap:10px}
.services a{flex:1;height:76px;border:1px solid var(--line);border-radius:6px;display:flex;align-items:center;justify-content:center;text-align:center;font-size:14px;font-weight:500;color:var(--brown);text-decoration:none;line-height:1.3;background:var(--white);box-shadow:0 2px 0 var(--line)}

.main{position:absolute;top:870px;left:120px;width:730px}
.features{height:390px;background:var(--cream);border-radius:8px;position:relative}
.features-badge{position:absolute;left:265px;top:-14px;width:200px;height:200px;border-radius:50%;background:var(--orange);color:var(--white);text-align:center;padding-top:36px;font-family:"M PLUS Rounded 1c",sans-serif}
.features-badge small{display:block;font-size:13px}
.features-badge strong{display:block;font-size:24px;font-weight:800;margin-top:4px}
.feature-list{position:absolute;left:30px;top:110px;width:670px;display:flex;gap:20px}
.feature{flex:1;height:240px;background:var(--orange);border-radius:6px;position:relative;padding:38px 16px 16px;color:var(--white);text-align:center}
.feature-num{position:absolute;left:50%;top:-20px;transform:translateX(-50%);width:40px;height:40px;border-radius:50%;background:var(--white);color:var(--orange);font-weight:800;font-size:20px;display:flex;align-items:center;justify-content:center;font-family:"M PLUS Rounded 1c",sans-serif}
.feature-lead{font-size:13px;line-height:1.5}
.feature-title{font-family:"M PLUS Rounded 1c",sans-serif;font-size:28px;font-weight:800;margin:6px 0 12px}
.feature-note{background:var(--white);color:var(--orange);border-radius:8px;padding:14px 8px;font-size:13px;line-height:1.5}

.greeting{margin-top:26px;border-top:3px solid var(--orange);padding-top:16px;position:relative;height:300px}
.section-title{font-size:19px;font-weight:700;color:var(--brown)}
.greeting p{width:410px;font-size:13px;line-height:1.9;margin-top:16px}
.greeting .sign{margin-top:14px;text-align:right;width:410px;font-size:13px}
.doctor-photo{position:absolute;right:20px;top:64px;width:250px;height:220px;background:linear-gradient(180deg,#eef3f4,#dfe7ea);border-radius:4px}

.news{margin-top:24px;border-top:1px solid var(--line);padding-top:16px}
.news .section-title{display:flex;align-items:center;gap:8px}
.news .section-title::before{content:"";width:6px;height:20px;background:var(--orange)}
.news ul{list-style:none;margin-top:14px}
.news li{display:flex;align-items:center;gap:24px;padding:14px 20px;border-bottom:1px dotted var(--line);font-size:13px}
.news .tag{background:var(--orange);color:var(--white);font-size:12px;padding:3px 10px;border-radius:3px}

.side{position:absolute;top:870px;left:880px;width:200px}
.side-photo{height:110px;background:linear-gradient(135deg,#e7f0f3,#f3e6d6);border-radius:4px}
.side-label{font-size:12px;text-align:center;margin:6px 0 12px;color:var(--brown)}
.side-banner{display:flex;align-items:center;gap:10px;border:2px solid var(--orange-soft);border-radius:6px;padding:10px;margin-bottom:10px;background:var(--white)}
.side-banner .icon{width:54px;height:54px;border-radius:50%;background:var(--orange-pale);flex:none}
.side-banner p{font-size:13px;line-height:1.4;color:var(--brown)}
.side-banner strong{color:var(--orange);font-size:16px;display:block}
.side-menu{margin-top:16px;border:1px solid var(--line)}
.side-menu h3{background:var(--cream);font-size:14px;color:var(--brown);padding:8px 12px;border-bottom:2px solid var(--orange)}
.side-menu li{list-style:none;font-size:13px;padding:7px 12px;border-bottom:1px dotted var(--line)}
.side-menu li::before{content:"▸ ";color:var(--orange)}
.side-deco{position:absolute;top:840px;left:120px;width:70px;height:70px;border-radius:50%;background:var(--orange-pale)}

.site-footer{position:absolute;top:1880px;left:0;width:1200px;height:400px;background:var(--cream);border-top:4px solid var(--orange)}
.foot-info{position:absolute;left:120px;top:40px}
.foot-name{font-family:"M PLUS Rounded 1c",sans-serif;font-weight:800;font-size:28px;color:var(--brown)}
.foot-info .addr{font-size:12px;margin-top:6px}
.foot-info .tel{justify-content:flex-start;margin-top:30px;font-size:34px}
.foot-info .hours-f{font-size:13px;line-height:1.7;margin-top:24px}
.map{position:absolute;left:480px;top:36px;width:600px;height:300px;background:linear-gradient(135deg,#e9eee6,#f2efe6);border:1px solid var(--line)}
</style>
</head>
<body>

<header class="site-header">
  <div class="brand">
    <div class="brand-tag">みどり県こもれび市の家族みんなで通える歯科医院</div>
    <div class="brand-name"><span class="brand-mark"></span>ひなた歯科クリニック</div>
  </div>
  <div class="hours">午前 9:00〜12:30<br>午後 2:00〜6:30（土曜午後 2:00〜5:00）<br>休診日：木・日・祝</div>
  <div class="contact">
    <small>TEL受付時間は診療時間内です</small>
    <div class="tel">
      <svg width="26" height="26" viewBox="0 0 24 24"><path fill="var(--orange)" d="M6.6 10.8a15 15 0 0 0 6.6 6.6l2.2-2.2a1 1 0 0 1 1-.25 11 11 0 0 0 3.6.6 1 1 0 0 1 1 1V20a1 1 0 0 1-1 1A17 17 0 0 1 3 4a1 1 0 0 1 1-1h3.5a1 1 0 0 1 1 1 11 11 0 0 0 .6 3.6 1 1 0 0 1-.25 1z"/></svg>
      0595-00-1234
    </div>
    <div class="addr">〒518-0000 みどり県こもれび市ひなた町1-2-3</div>
  </div>
</header>

<nav class="global-nav">
  <a href="#"><svg width="18" height="18" viewBox="0 0 24 24"><path fill="var(--brown)" d="M12 3 2 12h3v8h5v-5h4v5h5v-8h3z"/></svg></a>
  <a href="#">医院紹介</a><a href="#">診療内容</a><a href="#">院長紹介</a><a href="#">費用について</a><a href="#">患者様の声</a><a href="#">アクセス</a>
</nav>

<section class="hero">
  <div class="hero-side" style="left:0"></div>
  <div class="hero-main" role="img" aria-label="白衣の歯科医師が笑顔の女の子に話しかける明るい診療室の写真"></div>
  <div class="hero-side" style="right:0"></div>
  <p class="hero-copy"><span>自分の家族にもできる</span><br><span>安心安全な歯科医療を目指します</span></p>
</section>
<div class="dots"><i></i><i></i><i></i></div>

<nav class="services">
  <a href="#">一般歯科</a><a href="#">小児歯科</a><a href="#">義歯<br>(入れ歯)</a><a href="#">口腔外科</a><a href="#">インプラント</a><a href="#">審美歯科</a><a href="#">矯正歯科</a><a href="#">予防歯科</a>
</nav>

<main class="main">
  <section class="features">
    <div class="features-badge"><small>ひなた歯科クリニックの</small><strong>3つの特徴</strong></div>
    <div class="feature-list">
      <div class="feature">
        <div class="feature-num">1</div>
        <p class="feature-lead">被せ物の素材を<br>選べる</p>
        <p class="feature-title">セレクト</p>
        <p class="feature-note">ご予算やご希望に<br>合わせて選べます</p>
      </div>
      <div class="feature">
        <div class="feature-num">2</div>
        <p class="feature-lead">気になる部分だけ<br>短期間で</p>
        <p class="feature-title">プチ矯正</p>
        <p class="feature-note">目立ちにくい装置で<br>気軽に始められます</p>
      </div>
      <div class="feature">
        <div class="feature-num">3</div>
        <p class="feature-lead">成長期から<br>始める</p>
        <p class="feature-title">小児矯正</p>
        <p class="feature-note">お子様の成長に<br>合わせた治療です</p>
      </div>
    </div>
  </section>

  <section class="greeting">
    <h2 class="section-title">ご家族揃って安心して通える歯科医院を目指して…</h2>
    <p>この度、みどり県こもれび市に歯科医院を開院する運びとなりました。地域の皆様に信頼していただけるよう、一人ひとりのお口の状態に合わせた丁寧な説明と治療を心がけております。小さなお子様からご年配の方まで、ご家族みんなで気軽に通っていただける明るく清潔な医院づくりに努めてまいります。どうぞお気軽にご相談ください。</p>
    <p class="sign">院長　日向 一郎</p>
    <div class="doctor-photo" role="img" aria-label="白衣姿で腕を組む院長の写真"></div>
  </section>

  <section class="news">
    <h2 class="section-title">新着情報</h2>
    <ul>
      <li><span class="tag">お知らせ</span><time>2016/05/20</time><span>ホームページを公開いたしました。</span></li>
      <li><span class="tag">お知らせ</span><time>2016/05/10</time><span>開院日のご案内を掲載しました。</span></li>
      <li><span class="tag">お知らせ</span><time>2016/05/01</time><span>内覧会の日程が決まりました。</span></li>
    </ul>
  </section>
</main>

<aside class="side">
  <div class="side-photo" role="img" aria-label="明るい院内の待合室の写真"></div>
  <p class="side-label">院内のご案内</p>
  <div class="side-banner"><span class="icon"></span><p>初めての方へ<strong>ご来院の流れ</strong></p></div>
  <div class="side-banner"><span class="icon"></span><p>歯科医師<br><strong>衛生士 募集中!</strong></p></div>
  <div class="side-menu">
    <h3>診療項目</h3>
    <ul>
      <li>一般歯科</li><li>小児歯科</li><li>義歯(入れ歯)</li><li>口腔外科</li><li>インプラント</li><li>審美歯科</li><li>矯正歯科</li><li>予防歯科</li>
    </ul>
  </div>
  <div class="side-deco" role="img" aria-label="歯のキャラクターのイラスト"></div>
</aside>

<footer class="site-footer">
  <div class="foot-info">
    <div class="foot-name">ひなた歯科クリニック</div>
    <div class="addr">〒518-0000 みどり県こもれび市ひなた町1-2-3</div>
    <div class="tel">
      <svg width="30" height="30" viewBox="0 0 24 24"><path fill="var(--orange)" d="M6.6 10.8a15 15 0 0 0 6.6 6.6l2.2-2.2a1 1 0 0 1 1-.25 11 11 0 0 0 3.6.6 1 1 0 0 1 1 1V20a1 1 0 0 1-1 1A17 17 0 0 1 3 4a1 1 0 0 1 1-1h3.5a1 1 0 0 1 1 1 11 11 0 0 0 .6 3.6 1 1 0 0 1-.25 1z"/></svg>
      0595-00-1234
    </div>
    <div class="hours-f">午前 9:00〜12:30<br>午後 2:00〜6:30（土曜午後 2:00〜5:00）<br>休診日：木・日・祝</div>
  </div>
  <div class="map" role="img" aria-label="医院周辺の地図"></div>
</footer>

</body>
</html>
```